Accountant & CPA Website $100 bonus

We are designing a website for our client Willowmere Accountants and CPAs. They are a new business and looking for a clean, modern website. The services they offer are siilar to: https://www.brx-tal.com/index.htm

We would like to see designs that use the black and the green mostly, with a hint of purple and grey. However, we do like to give our designers the freedom to be creative. If you see a different vison, feel free to express that.

Number of Pages Required

1 page

Font styles to use
Sans Serif

```html
<!DOCTYPE html>
<html lang="en">
<head>
<meta charset="utf-8">
<title>Willowmere Accountants &amp; CPAs</title>
<link href="https://fonts.googleapis.com/css2?family=Nunito:wght@400;600;700&family=Saira+Condensed:wght@300;400&display=swap" rel="stylesheet">
<style>
:root{
  --green:#7d9b2b;
  --green-dark:#5f7a1c;
  --black:#000;
  --charcoal:#1d1d1d;
  --grey-bar:#3a3a3a;
  --grey-light:#efefef;
  --purple:#6a4fb8;
  --text:#333;
  --muted:#777;
  --white:#fff;
  --light-text:#e6e6e6;
}
*{margin:0;padding:0;box-sizing:border-box}
html,body{width:1200px;height:2955px;overflow:hidden}
body{position:relative;font-family:"Nunito",sans-serif;color:var(--text);background:var(--white)}
.abs{position:absolute}
.heading{font-family:"Saira Condensed",sans-serif;font-weight:400;text-transform:uppercase;letter-spacing:1.5px}

.topbar{left:0;top:0;width:1200px;height:30px;background:var(--grey-bar);color:#ddd;font-size:11px;letter-spacing:.5px}
.topbar .addr{position:absolute;left:30px;top:8px}
.topbar .phone{position:absolute;right:30px;top:4px;font-size:17px;letter-spacing:1.5px;color:#fff;display:flex;align-items:center;gap:8px}

.nav{left:0;top:30px;width:1200px;height:70px;background:var(--black)}
.nav .brand{position:absolute;left:40px;top:22px;display:flex;align-items:center;gap:8px;color:var(--green);font-size:22px;font-weight:700;letter-spacing:1px}
.brand .dot{width:14px;height:14px;background:var(--purple);border-radius:50%}
.nav .menu{position:absolute;left:393px;top:0;height:70px;width:570px;background:#111}
.menu a{position:absolute;top:30px;color:#ddd;font-size:11px;letter-spacing:1.4px;text-decoration:none;text-transform:uppercase}
.menu a::after{content:"";display:inline-block;width:5px;height:5px;border-right:1.5px solid #ddd;border-bottom:1.5px solid #ddd;transform:rotate(45deg);margin-left:8px;position:relative;top:-3px}
.menu .active{background:#2e2e2e;top:10px;height:60px;padding:20px 10px 0;border-radius:4px 4px 0 0}
.menu .active::after{transform:rotate(-135deg);top:0}
.nav .cta{position:absolute;left:962px;top:0;width:238px;height:70px;background:var(--green);color:#111;font-size:16px;font-weight:600;letter-spacing:.8px;display:flex;align-items:center;justify-content:center}

.dropdown{left:727px;top:100px;width:241px;height:194px;background:var(--white);border:1px solid #ddd;border-bottom:3px solid var(--green);border-radius:0 0 6px 6px;z-index:5}
.dropdown li{list-style:none;position:absolute;left:18px;font-size:10.5px;letter-spacing:1.4px;text-transform:uppercase;color:#333}
.dropdown .current{left:14px;width:210px;height:26px;background:#f2f2f2;border-bottom:1px solid var(--green);padding:7px 5px}
.dropdown .current::after{content:"";position:absolute;right:8px;top:9px;width:5px;height:5px;border-right:1.5px solid var(--green);border-top:1.5px solid var(--green);transform:rotate(45deg)}

.hero{left:0;top:100px;width:1200px;height:405px;background:linear-gradient(180deg,#8a8580 0%,#5a5752 40%,#2f2e2d 80%,#232322 100%)}
.hero-tab{left:189px;top:468px;width:258px;height:37px;background:var(--white);border-top:2px solid var(--purple);border-radius:6px 6px 0 0;font-size:12.5px;letter-spacing:1.6px;display:flex;align-items:center;justify-content:center;color:#222}

.intro{left:0;top:505px;width:1200px;height:475px;background:linear-gradient(180deg,#fff 0%,#f5f5f5 60%,#ececec 100%)}
.intro h1{position:absolute;left:190px;top:25px;font-size:25px;color:#444;letter-spacing:1.8px}
.btn-outline{position:absolute;border:1.5px solid var(--green);border-radius:4px;color:#555;font-size:10px;letter-spacing:1.6px;text-transform:uppercase;display:flex;align-items:center;justify-content:center}
.intro .all{left:855px;top:27px;width:155px;height:24px}
.intro .all::after{content:"";width:5px;height:5px;border-right:1.5px solid #333;border-top:1.5px solid #333;transform:rotate(45deg);margin-left:10px}
.intro .copy{position:absolute;left:190px;top:123px;width:466px;font-size:10px;line-height:15px;color:#444}
.intro .copy p{margin-bottom:10px}
.intro .name{position:absolute;left:190px;top:376px;font-size:19px;color:#222;letter-spacing:1.8px}
.intro .role{position:absolute;left:190px;top:401px;font-size:9.5px;color:#666}
.portrait{left:750px;top:610px;width:260px;height:326px;border-radius:10px;background:linear-gradient(180deg,#f4f4f4 0%,#cfcfcf 55%,#8d8d8d 100%);box-shadow:0 8px 20px rgba(0,0,0,.25)}

.services{left:0;top:980px;width:1200px;height:1155px;background:linear-gradient(180deg,#191919 0%,#2a2a2a 50%,#363636 100%);color:var(--light-text)}
.services h2{position:absolute;left:0;width:1200px;top:52px;text-align:center;font-size:25px;letter-spacing:2px;color:var(--white)}
.services .sub{position:absolute;left:0;width:1200px;top:105px;text-align:center;font-size:15px;letter-spacing:.6px;color:#ddd}
.svc-photo{position:absolute;width:330px;height:199px;border-radius:8px;border:1px solid #666;box-shadow:0 6px 18px rgba(0,0,0,.4)}
.svc-text{position:absolute;width:400px}
.svc-text h3{font-size:19px;letter-spacing:1.8px;margin-bottom:12px;color:var(--white)}
.svc-text p{font-size:9.8px;line-height:15px;color:#ccc;margin-bottom:20px;letter-spacing:.2px}
.svc-btns{display:flex;gap:20px}
.svc-btns span{width:190px;height:19px;border-radius:3px;font-size:9.5px;font-weight:700;letter-spacing:.6px;display:flex;align-items:center;justify-content:center;color:var(--green)}
.svc-btns .solid{background:var(--white)}
.svc-btns .line{border:1px solid var(--green)}

.consult{left:0;top:2135px;width:1200px;height:470px;background:linear-gradient(180deg,#f3f3f3 0%,#e6e6e6 100%)}
.consult h2{position:absolute;left:0;width:1200px;top:50px;text-align:center;font-size:25px;color:#222;letter-spacing:1.8px}
.consult .sub{position:absolute;left:0;width:1200px;top:104px;text-align:center;font-size:15px;line-height:30px;color:#444;letter-spacing:.6px}
.field{position:absolute}
.field label{display:block;font-size:10px;letter-spacing:1.6px;color:#222;margin:0 0 5px 10px}
.field .box{height:30px;background:var(--white);border:1px solid #bbb;border-radius:4px;font-size:10px;color:#999;padding:8px 10px;position:relative}
.field .box.filled{color:#222;border-color:#aaa}
.field .box svg{position:absolute;right:10px;top:8px}
.send{left:470px;top:2530px;width:260px;height:29px;background:var(--green);color:#fff;font-size:15px;letter-spacing:.8px;border-radius:3px;display:flex;align-items:center;justify-content:center}

.footer{left:0;top:2605px;width:1200px;height:305px;background:#222;color:#ddd}
.footer .brand{position:absolute;left:190px;top:45px;display:flex;align-items:center;gap:8px;color:var(--green);font-size:21px;font-weight:700;letter-spacing:1px}
.footer .firm{position:absolute;left:190px;top:93px;font-size:12.5px;color:#fff;letter-spacing:.5px}
.footer .contact{position:absolute;left:190px;display:flex;gap:14px;font-size:12.5px;line-height:20px;letter-spacing:.5px;color:#eee}
.footer .socials{position:absolute;left:190px;top:241px;display:flex;gap:15px}
.footer .socials span{width:20px;height:20px;border-radius:50%;border:2px solid #ccc}
.fcol{position:absolute;top:40px}
.fcol h4{font-weight:400;font-size:13px;letter-spacing:1.8px;color:#fff;text-transform:uppercase;border-bottom:1px solid #ddd;display:inline-block;padding-bottom:2px;margin-bottom:18px}
.fcol li{list-style:none;font-size:12.5px;letter-spacing:.5px;line-height:30px;color:#ddd}
.fcol li.hl{color:var(--green)}
.legal{left:0;top:2910px;width:1200px;height:45px;background:var(--grey-bar);color:#ccc;font-size:9px;letter-spacing:.3px}
.legal .copy{position:absolute;left:190px;top:15px;display:flex;gap:8px;align-items:center}
.legal .links{position:absolute;right:192px;top:16px}
</style>
</head>
<body>

<div class="abs topbar">
  <span class="addr">4820, Harbor Street, New York</span>
  <span class="phone"><svg width="14" height="14" viewBox="0 0 24 24"><path d="M6.6 10.8a15.5 15.5 0 0 0 6.6 6.6l2.2-2.2c.3-.3.7-.4 1-.2 1.1.4 2.3.6 3.6.6.6 0 1 .4 1 1V20c0 .6-.4 1-1 1A17 17 0 0 1 3 4c0-.6.4-1 1-1h3.5c.6 0 1 .4 1 1 0 1.3.2 2.5.6 3.6.1.3 0 .7-.2 1z" fill="#7d9b2b"/></svg>555-014-2290</span>
</div>

<header class="abs nav">
  <div class="brand"><span class="dot"></span>WILLOWMERE</div>
  <nav class="menu">
    <a style="left:25px">Tax Services</a>
    <a style="left:155px">Accounting Services</a>
    <a class="active" style="left:334px">Industries</a>
    <a style="left:462px">About Us</a>
  </nav>
  <div class="cta">Get a Free Consultation</div>
</header>

<ul class="abs dropdown">
  <li style="top:13px">Healthcare</li>
  <li style="top:43px">Online Retail &amp; Ecommerce</li>
  <li class="current" style="top:70px">Real Estate</li>
  <li style="top:108px">Technology</li>
  <li style="top:138px">Wholesale Manufacturing</li>
  <li style="top:168px">Industries We Serve</li>
</ul>

<div class="abs hero" role="img" aria-label="Aerial photograph of the New York skyline at dusk"></div>
<div class="abs hero-tab">TAX AND ACCOUNTING SERVICES</div>

<section class="abs intro">
  <h1 class="heading">For Businesses and Individuals in New York</h1>
  <div class="all btn-outline">All Our Services</div>
  <div class="copy">
    <p>Aut quae, and ad, yet aperiam. Ullam sint. Aliquam et. Tempora veniam. Lorem. Eiusmod dolores exercitationem. Illo inventore, so eaque. Dolore. Labore anim id, or illo. Do quis, but iure dolore ab, yet qui. Minima velit id, nor minim. Esse nisi, or nequeporro. Aut sint commodi, nor consequatur, and quo explicabo ab. Sint adipisci. Iure anim ipsam.</p>
    <p>Do nulla, yet proident, but illo, or pariatur. Id lorem, and minima, for officia. Deserunt.Amet consequuntur quam nulla, so officia. Incididunt exercitation eos. Dolore unde, or magni nulla, and aperiam, yet quae. Ipsam ea, and modi. Velit. Incidunt amet, or odit irure, or adipisci. Velit dolores. Perspiciatis. Perspiciatis ex anim explicabo commodi ex, minima. Voluptas qui, or sint quia ullam illo. Ipsa do, for incidunt, for laboriosam, but aliquid.</p>
    <p>Do nulla, yet proident, but illo, or pariatur. Id lorem, and minima, for officia. Deserunt.Amet consequuntur quam nulla, so officia. Incididunt exercitation eos. Dolore unde, or magni nulla, and aperiam, yet quae. Ipsam ea, and modi. Velit. Incidunt amet, or odit irure, or adipisci. Velit dolores. Perspiciatis. Perspiciatis ex anim explicabo commodi ex, minima. Voluptas qui, or sint quia ullam illo. Ipsa do, for incidunt, for laboriosam, but aliquid.</p>
  </div>
  <div class="name heading">Marcus Ellery</div>
  <div class="role">CEO, Willowmere Accountants &amp; CPAs</div>
</section>
<div class="abs portrait" role="img" aria-label="Black and white photograph of the CEO in a suit standing in a white hallway"></div>

<section class="abs services">
  <h2 class="heading">Our Services</h2>
  <div class="sub">All your accounting needs completed perfectly.</div>

  <div class="svc-photo" style="left:190px;top:170px;background:linear-gradient(135deg,#6b6b6b 0%,#d9d6cf 45%,#c49a65 100%)" role="img" aria-label="Tax form with a pen on a wooden desk"></div>
  <div class="svc-text" style="left:610px;top:193px">
    <h3 class="heading">Tax Services</h3>
    <p>Aut quae, and ad, yet aperiam. Ullam sint. Aliquam et. Tempora veniam. Lorem. Eiusmod dolores exercitationem. Illo inventore, so eaque. Dolore. Labore anim id, or illo. Do quis, but iure dolore ab, yet qui. Minima velit id, nor minim. Esse nisi, or nequeporro. Aut sint commodi, nor consequatur, and quo explicabo ab. Sint adipisci. Iure anim ipsam.</p>
    <div class="svc-btns"><span class="solid">View Tax Services</span><span class="line">Read More</span></div>
  </div>

  <div class="svc-text" style="left:190px;top:433px">
    <h3 class="heading">Accounting Services</h3>
    <p>Aut quae, and ad, yet aperiam. Ullam sint. Aliquam et. Tempora veniam. Lorem. Eiusmod dolores exercitationem. Illo inventore, so eaque. Dolore. Labore anim id, or illo. Do quis, but iure dolore ab, yet qui. Minima velit id, nor minim. Esse nisi, or nequeporro. Aut sint commodi, nor consequatur, and quo explicabo ab. Sint adipisci. Iure anim ipsam.</p>
    <div class="svc-btns"><span class="solid">View Accounting Services</span><span class="line">Read More</span></div>
  </div>
  <div class="svc-photo" style="left:680px;top:410px;background:linear-gradient(135deg,#e8e8e8 0%,#cfcfcf 50%,#e9e2c4 100%)" role="img" aria-label="Financial documents and a notepad on a white wooden table"></div>

  <div class="svc-photo" style="left:190px;top:650px;background:linear-gradient(135deg,#f2f2f2 0%,#b9b9b9 50%,#5a4a3f 100%)" role="img" aria-label="Hands typing on a laptop showing charts"></div>
  <div class="svc-text" style="left:610px;top:673px">
    <h3 class="heading">Niche Services</h3>
    <p>Aut quae, and ad, yet aperiam. Ullam sint. Aliquam et. Tempora veniam. Lorem. Eiusmod dolores exercitationem. Illo inventore, so eaque. Dolore. Labore anim id, or illo. Do quis, but iure dolore ab, yet qui. Minima velit id, nor minim. Esse nisi, or nequeporro. Aut sint commodi, nor consequatur, and quo explicabo ab. Sint adipisci. Iure anim ipsam.</p>
    <div class="svc-btns"><span class="solid">View Niche Services</span><span class="line">Read More</span></div>
  </div>

  <div class="svc-text" style="left:190px;top:913px">
    <h3 class="heading">Ledgerline Accounting</h3>
    <p>Aut quae, and ad, yet aperiam. Ullam sint. Aliquam et. Tempora veniam. Lorem. Eiusmod dolores exercitationem. Illo inventore, so eaque. Dolore. Labore anim id, or illo. Do quis, but iure dolore ab, yet qui. Minima velit id, nor minim. Esse nisi, or nequeporro. Aut sint commodi, nor consequatur, and quo explicabo ab. Sint adipisci. Iure anim ipsam.</p>
    <div class="svc-btns"><span class="solid">View Ledgerline Services</span><span class="line">Read More</span></div>
  </div>
  <div class="svc-photo" style="left:680px;top:890px;background:linear-gradient(135deg,#4a3a2e 0%,#262626 50%,#8a6a4b 100%)" role="img" aria-label="Person working on a laptop with accounting software on a wooden desk"></div>
</section>

<section class="abs consult">
  <h2 class="heading">Get a Free Consultation Today!</h2>
  <div class="sub">Contact us today with your details and we can<br>send you details on how we can help you.</div>

  <div class="field" style="left:190px;top:189px;width:244px">
    <label>NAME*</label>
    <div class="box filled">Marcu|<svg width="13" height="13" viewBox="0 0 24 24" fill="none" stroke="#7d9b2b" stroke-width="2"><circle cx="12" cy="8" r="4"/><path d="M4 21c1-4 4-6 8-6s7 2 8 6"/></svg></div>
  </div>
  <div class="field" style="left:470px;top:189px;width:244px">
    <label>EMAIL*</label>
    <div class="box">user@example.com<svg width="14" height="13" viewBox="0 0 24 24" fill="none" stroke="#888" stroke-width="1.6"><rect x="3" y="5" width="18" height="14" rx="1"/><path d="M3 6l9 7 9-7"/></svg></div>
  </div>
  <div class="field" style="left:750px;top:189px;width:260px">
    <label>PHONE NUMBER</label>
    <div class="box">123 456 7890<svg width="13" height="13" viewBox="0 0 24 24" fill="none" stroke="#888" stroke-width="1.6"><path d="M6.6 10.8a15.5 15.5 0 0 0 6.6 6.6l2.2-2.2c.3-.3.7-.4 1-.2 1.1.4 2.3.6 3.6.6.6 0 1 .4 1 1V20c0 .6-.4 1-1 1A17 17 0 0 1 3 4c0-.6.4-1 1-1h3.5c.6 0 1 .4 1 1 0 1.3.2 2.5.6 3.6.1.3 0 .7-.2 1z"/></svg></div>
  </div>
  <div class="field" style="left:190px;top:264px;width:820px">
    <label>YOUR MESSAGE*</label>
    <div class="box" style="height:89px">Your message here...</div>
  </div>
</section>
<div class="abs send">Send Message</div>

<footer class="abs footer">
  <div class="brand"><span class="dot" style="width:13px;height:13px;background:var(--purple);border-radius:50%"></span>WILLOWMERE</div>
  <div class="firm">Willowmere Accountants &amp; CPAs</div>
  <div class="contact" style="top:128px">
    <svg width="22" height="24" viewBox="0 0 24 24" style="margin-top:14px"><path d="M12 2a7 7 0 0 0-7 7c0 5 7 13 7 13s7-8 7-13a7 7 0 0 0-7-7zm0 9.5A2.5 2.5 0 1 1 12 6.5a2.5 2.5 0 0 1 0 5z" fill="#fff"/></svg>
    <span>Suite 410,<br>88 Linden Ave,<br>New York, NY 10002</span>
  </div>
  <div class="contact" style="top:194px">
    <svg width="24" height="24" viewBox="0 0 24 24"><path d="M6.6 10.8a15.5 15.5 0 0 0 6.6 6.6l2.2-2.2c.3-.3.7-.4 1-.2 1.1.4 2.3.6 3.6.6.6 0 1 .4 1 1V20c0 .6-.4 1-1 1A17 17 0 0 1 3 4c0-.6.4-1 1-1h3.5c.6 0 1 .4 1 1 0 1.3.2 2.5.6 3.6.1.3 0 .7-.2 1z" fill="#fff"/></svg>
    <span>555 014 2290</span>
  </div>
  <div class="socials"><span></span><span></span><span></span></div>

  <div class="fcol" style="left:400px">
    <h4>Tax Services</h4>
    <ul><li>Tax Planning</li><li>Tax Preparation</li><li class="hl">International Tax Services</li><li>IRS Tax Problem Resolution</li><li>Our Tax Services</li></ul>
  </div>
  <div class="fcol" style="left:610px">
    <h4>Accounting</h4>
    <ul><li>Incorporation Services</li><li>Outsourced CFO Services</li><li>Ledgerline Accounting</li><li>Small Business Accounting</li><li>Our Accounting Services</li></ul>
  </div>
  <div class="fcol" style="left:820px">
    <h4>Industries</h4>
    <ul><li>Healthcare</li><li>Online Retail &amp; e-Commerce</li><li>Real Estate Accounting</li><li>Technology</li><li>Wholesale Manufacturing</li><li>Industries We Serve</li></ul>
  </div>
</footer>

<div class="abs legal">
  <div class="copy"><svg width="14" height="14" viewBox="0 0 24 24" fill="none" stroke="#ccc" stroke-width="1.6"><circle cx="12" cy="12" r="10"/><path d="M15 9a4 4 0 1 0 0 6"/></svg>2023 Willowmere Accountants &amp; CPAs. All Rights Reserved.</div>
  <div class="links">Terms and Conditions &nbsp;&nbsp;•&nbsp;&nbsp; Privacy Policy</div>
</div>

</body>
</html>
```